E-commerce Website Trevalin.com

Work Required
Homepage: Creation of an attractive design, clearly presenting product categories (recovery mixes, detox, etc., herbal candies).
Product Page: Highlight products with detailed information, use of mockups to represent the products.
Logo: Design a logo representative of Trevalin.com, naturally evoking the equestrian field and the organic aspect of the products.

Target Market(s)

show pdf in documents

Industry/Entity Type

show pdf in documents

Coding

Coded - Design and coding required

Requirements
Must have
• show pdf in documents
Nice to have
• show pdf in documents
Should not have
• show pdf in documents

```html
<!DOCTYPE html>
<html lang="en">
<head>
<meta charset="utf-8">
<title>Trevalin.com – Brand Board &amp; Homepage</title>
<link rel="stylesheet" href="https://fonts.googleapis.com/css2?family=Crimson+Text:wght@400&family=Manrope:wght@400;500;600&display=swap">
<style>
:root{
  --board:#b3b3b3;
  --frame:#4f4f4f;
  --teal:#4b7472;
  --orange:#ecab4e;
  --sand:#ece8e1;
  --ink:#1f1f1f;
  --muted:#4a4a4a;
  --white:#ffffff;
  --topbar:#1c1c1c;
  --line:#d9d9d9;
  --mint:#dfe9e5;
}
*{box-sizing:border-box;margin:0;padding:0}
html,body{width:925px;height:1200px;overflow:hidden;background:var(--board);font-family:"Manrope",sans-serif;color:var(--ink)}
body{position:relative}

/* brand board */
.brand-board{position:absolute;left:17px;top:37px;width:891px;height:222px;border:2px solid var(--frame);border-radius:10px;overflow:hidden;display:grid;grid-template-columns:1fr 1fr;grid-template-rows:1fr 1fr}
.lockup-tile{display:flex;align-items:center;justify-content:center;gap:10px}
.lockup-tile .mark{width:50px;height:50px;border-radius:50%;flex:none}
.lockup-tile .name{font-family:"Crimson Text",serif;font-size:44px;line-height:1}
.tile-teal{background:var(--teal)} .tile-teal .mark{border:2px solid var(--orange)} .tile-teal .name{color:var(--white)}
.tile-orange{background:var(--orange)} .tile-orange .mark{border:2px solid var(--ink)} .tile-orange .name{color:var(--ink)}
.tile-white{background:var(--white)} .tile-white .mark{background:var(--orange)}
.tile-sand{background:var(--sand)} .tile-sand .mark{background:var(--orange)}

/* website */
.site{position:absolute;left:17px;top:290px;width:891px;height:910px;border:2px solid var(--frame);border-bottom:none;border-radius:10px 10px 0 0;overflow:hidden;background:var(--white)}
.announce{height:33px;background:var(--topbar);color:#e6e6e6;font-size:10.5px;display:flex;align-items:center;justify-content:center;gap:11px}
.announce a{color:#e6e6e6}
.header{height:73px;position:relative;border-bottom:1px solid var(--line)}
.header .logo{position:absolute;left:81px;top:25px;display:flex;align-items:center;gap:6px}
.header .logo .mark{width:23px;height:23px;border-radius:50%;background:var(--orange)}
.header .logo .name{font-family:"Crimson Text",serif;font-size:19px}
.search{position:absolute;left:310px;top:20px;width:270px;height:34px;border:1px solid #bdbdbd;border-radius:17px;display:flex;align-items:center;padding-left:15px;gap:10px;color:#7a7a7a;font-size:10.5px}
.pill{position:absolute;top:20px;height:34px;border-radius:17px;display:flex;align-items:center;justify-content:center;gap:8px;font-size:10.5px}
.account{left:601px;width:110px;border:1px solid #bdbdbd;color:var(--muted)}
.cart{left:720px;width:96px;background:var(--teal);color:var(--white)}
.nav{height:47px;display:flex;justify-content:center;align-items:center;gap:38px;font-size:10.5px;color:#333}
.nav span{display:flex;align-items:center;gap:5px}

.hero{height:329px;background:var(--sand);position:relative}
.hero h1{position:absolute;left:138px;top:52px;font-size:41px;line-height:37px;font-weight:600;letter-spacing:-1px;width:340px}
.hero p{position:absolute;left:138px;top:180px;font-size:10px;line-height:14px;color:#3a3a3a;width:250px}
.btn{position:absolute;left:138px;top:226px;width:111px;height:34px;border-radius:17px;background:var(--teal);color:var(--white);font-size:10.5px;display:flex;align-items:center;justify-content:center}
.hero-photo{position:absolute;left:483px;top:25px;width:268px;height:268px;border-radius:50%;background:radial-gradient(circle at 35% 45%,#7a3c1e 0%,#9a5a34 30%,#2e4f8f 62%,#d3cab8 80%)}
.dots{position:absolute;left:0;right:0;top:311px;display:flex;justify-content:center;gap:5px}
.dots i{width:13px;height:3px;border-radius:2px;background:#c9c4bb}
.dots i.on{background:var(--ink)}

.products{position:relative;height:428px}
.products h2{position:absolute;left:0;right:0;top:42px;text-align:center;font-size:15px;font-weight:500}
.card-feature{position:absolute;left:138px;top:81px;width:284px;height:313px;border-radius:8px;overflow:hidden;background:var(--mint)}
.card-feature .shot{height:231px;background:radial-gradient(circle at 55% 45%,#ffffff 0%,#e9ecea 40%,#c9cecb 100%)}
.card-feature .body{padding:14px 18px}
.card-row{position:absolute;left:434px;width:319px;height:151px;border-radius:8px;overflow:hidden;background:var(--sand);display:flex}
.card-row .shot{width:143px;flex:none}
.card-row .body{padding:0 19px;display:flex;flex-direction:column;justify-content:center}
.shot-tan{background:radial-gradient(circle at 55% 45%,#c9ae7f 0%,#e7dccb 45%,#f3f1ec 100%)}
.shot-cream{background:radial-gradient(circle at 55% 45%,#e9e4d8 0%,#f1efea 50%,#f6f5f2 100%)}
.card-title{font-size:13.5px;font-weight:500;margin-bottom:6px}
.card-text{font-size:10px;line-height:14px;color:var(--muted)}
</style>
</head>
<body>

<section class="brand-board">
  <div class="lockup-tile tile-teal"><span class="mark"></span><span class="name">Trevalin</span></div>
  <div class="lockup-tile tile-orange"><span class="mark"></span><span class="name">Trevalin</span></div>
  <div class="lockup-tile tile-white"><span class="mark"></span><span class="name">Trevalin</span></div>
  <div class="lockup-tile tile-sand"><span class="mark"></span><span class="name">Trevalin</span></div>
</section>

<main class="site">
  <div class="announce">Lorem ipsum dolor sit amet consectetur. <a href="#">1234567890</a></div>

  <header class="header">
    <div class="logo"><span class="mark"></span><span class="name">Trevalin</span></div>
    <div class="search">
      <svg width="13" height="13" viewBox="0 0 13 13" fill="none" stroke="#444" stroke-width="1.6"><circle cx="5.5" cy="5.5" r="4.2"/><path d="M8.6 8.6L12 12"/></svg>
      Search for..
    </div>
    <div class="pill account">
      <svg width="12" height="12" viewBox="0 0 12 12" fill="none" stroke="#444" stroke-width="1.2"><circle cx="6" cy="3.6" r="2.4"/><path d="M1.5 11.2c0-2.4 2-3.8 4.5-3.8s4.5 1.4 4.5 3.8z"/></svg>
      My Account
    </div>
    <div class="pill cart">
      <svg width="12" height="12" viewBox="0 0 12 12" fill="none" stroke="#fff" stroke-width="1.2"><rect x="1.5" y="3.5" width="9" height="7.5" rx="1"/><path d="M4 5V3a2 2 0 0 1 4 0v2"/></svg>
      My Cart
    </div>
  </header>

  <nav class="nav">
    <span>Digestion</span>
    <span>Organic <svg width="8" height="5" viewBox="0 0 8 5" fill="none" stroke="#333" stroke-width="1.2"><path d="M1 1l3 3 3-3"/></svg></span>
    <span>Catalog <svg width="8" height="5" viewBox="0 0 8 5" fill="none" stroke="#333" stroke-width="1.2"><path d="M1 1l3 3 3-3"/></svg></span>
    <span>Our Expertise</span>
    <span>Blog</span>
    <span>Contact</span>
  </nav>

  <section class="hero">
    <h1>Organic Food Supplements for Your Horses</h1>
    <p>Lorem ipsum dolor sit amet consectetur. Facilisis phasellus pharetra quisque ut leo bibendum.</p>
    <a class="btn">Shop Now</a>
    <div class="hero-photo" role="img" aria-label="Photo of a chestnut horse with a woman in a blue jacket holding its lead rope"></div>
    <div class="dots"><i class="on"></i><i></i><i></i></div>
  </section>

  <section class="products">
    <h2>Our Products</h2>
    <article class="card-feature">
      <div class="shot" role="img" aria-label="Product mockup of a white supplement bucket with a teal lid"></div>
      <div class="body">
        <div class="card-title">Organic Food</div>
        <div class="card-text">Lorem ipsum dolor sit amet consectetur. Facilisis phasellus pharetra quisque ut leo bibendum.</div>
      </div>
    </article>
    <article class="card-row" style="top:81px">
      <div class="shot shot-tan" role="img" aria-label="Product mockup of a tan supplement bucket"></div>
      <div class="body">
        <div class="card-title">Digestion Food</div>
        <div class="card-text">Lorem ipsum dolor sit amet consectetur. Facilisis phasellus pharetra quisque ut leo bibendum.</div>
      </div>
    </article>
    <article class="card-row" style="top:244px">
      <div class="shot shot-cream" role="img" aria-label="Product mockup of a white bucket with a tan lid"></div>
      <div class="body">
        <div class="card-title">Organic Herbs in Bulk</div>
        <div class="card-text">Lorem ipsum dolor sit amet consectetur. Facilisis phasellus pharetra quisque ut leo bibendum.</div>
      </div>
    </article>
  </section>
</main>

</body>
</html>
```